Lawyers in the Netherlands website + logo

We are going in 2015 to launch a website where all law firms in the Netherlands and have the opportunity to place an ad program.

The domain name wil be:

kwelderhofpunt.website

We want a responsive PSD bootstrap twitter 1170 pixel grid.
for the homepage, result page and the detail page of the customer.

This sites we like:
https://www.vorqami.com/lawyers

https://lawyers.vorqami.com/lawyer/tad-mirske-5820734

http://solicitordirectory.brevmoor.co.uk/
Map of the Netherlands?

http://solicitordirectory.brevmoor.co.uk/listing/category-search/commercial
http://www.quellbarn.com.au/find-a-lawyer/banking-finance-law/

```html
<!DOCTYPE html>
<html lang="en">
<head>
<meta charset="utf-8">
<title>Kwelderhof Punt – Helping you with your legal needs</title>
<link rel="stylesheet" href="https://fonts.googleapis.com/css2?family=Lato:wght@400;700;900&display=swap">
<style>
:root{
  --navy:#132f63;
  --navy-deep:#0d2552;
  --navy-bar:#1a3a70;
  --orange:#e8711a;
  --text:#2b2b2b;
  --muted:#6c6c6c;
  --line:#d8d8d8;
  --white:#ffffff;
  --map:#b7cde0;
}
*{box-sizing:border-box;margin:0;padding:0}
html,body{width:1200px;height:2478px;overflow:hidden;background:var(--white)}
body{font-family:"Lato",sans-serif;color:var(--text);position:relative}
a{color:inherit;text-decoration:none}

/* header */
.site-header{position:absolute;left:0;top:0;width:1200px;height:76px;background:var(--navy);border-bottom:3px solid var(--orange)}
.brand{position:absolute;left:74px;top:20px;font-weight:900;font-size:30px;letter-spacing:.5px;color:var(--white);text-transform:uppercase}
.btn{display:flex;align-items:center;justify-content:center;background:var(--orange);color:var(--white);font-weight:700}
.btn-listed{position:absolute;left:946px;top:16px;width:180px;height:40px;font-size:17px}
.main-nav{position:absolute;left:0;top:76px;width:1200px;height:30px;background:var(--navy-bar);font-size:13px;font-weight:700;color:var(--white)}
.main-nav a{position:absolute;top:0;height:30px;line-height:30px;padding:0 8px}
.main-nav .is-active{background:var(--orange)}

/* hero */
.hero{position:absolute;left:0;top:106px;width:1200px;height:618px;background:linear-gradient(100deg,#c9ccd0 0%,#e9eaea 35%,#d9d2c8 60%,#c9c3bb 100%)}
.hero-panel{position:absolute;left:74px;top:204px;width:540px;height:336px;background:rgba(24,52,110,.85);padding:26px}
.hero-title{color:var(--white);font-size:40px;font-weight:400;line-height:50px}
.field{position:absolute;background:var(--white);color:#8a8a8a;font-size:21px;display:flex;align-items:center;padding-left:26px}
.field-search{left:26px;top:122px;width:486px;height:64px}
.field-province{left:26px;top:214px;width:282px;height:66px}
.caret{position:absolute;right:20px;top:26px}
.btn-search{position:absolute;left:332px;top:214px;width:180px;height:66px;font-size:22px;gap:10px}

/* finders */
.finder-title{position:absolute;font-size:26px;font-weight:700;color:var(--navy)}
.finder-note{position:absolute;left:74px;top:816px;font-size:11px;color:var(--muted)}
.select-small{position:absolute;left:74px;top:842px;width:244px;height:40px;border:1px solid var(--line);font-size:16px;color:#8a8a8a;display:flex;align-items:center;padding-left:10px}
.btn-go{position:absolute;left:326px;top:842px;width:80px;height:40px;font-size:19px}
.map-placeholder{position:absolute;left:72px;top:914px;width:362px;height:392px;background:radial-gradient(ellipse at 50% 50%,#a9c2d9 0%,#c5d7e6 60%,#ffffff 100%);border-radius:40% 45% 35% 50%}
.divider{position:absolute;left:522px;top:754px;width:1px;height:616px;background:var(--line)}
.practice-list{position:absolute;left:572px;width:560px;display:grid;grid-template-columns:178px 228px 154px;font-size:13px;line-height:26px;list-style:none}
.practice-list .more{color:var(--orange)}

/* info band */
.info-band{position:absolute;left:0;top:1410px;width:1200px;height:460px;background:linear-gradient(180deg,#173a72 0%,#0f2c5e 100%);color:var(--white);text-align:center}
.info-band h2{position:absolute;left:0;top:86px;width:1200px;font-size:30px;font-weight:700}
.feature{position:absolute;top:186px;width:360px}
.feature svg{display:block;margin:0 auto 22px}
.feature h3{font-size:23px;font-weight:400;margin-bottom:10px}
.feature p{font-size:13px;font-weight:700;line-height:20px;padding:0 30px}

/* claim */
.claim-title{position:absolute;left:0;top:1942px;width:1200px;text-align:center;font-size:28px;font-weight:700;color:var(--navy)}
.claim-text{position:absolute;left:160px;top:2002px;width:880px;text-align:center;font-size:13px;line-height:24px;color:var(--muted)}
.btn-claim{position:absolute;left:498px;top:2086px;width:204px;height:54px;font-size:18px}
.rule{position:absolute;left:74px;top:2194px;width:1052px;height:2px;background:var(--line)}

/* footer */
.footer-col{position:absolute;top:2236px}
.footer-col h4{font-size:18px;font-weight:700;color:var(--navy);margin-bottom:10px}
.footer-col ul{list-style:none;font-size:13px;line-height:26px}
.footer-note{font-size:11px;color:var(--muted)}
.news-form{display:flex;margin-top:6px}
.news-input{width:172px;height:28px;border:1px solid var(--line);font-size:10px;color:#999;display:flex;align-items:center;padding-left:8px}
.news-send{width:56px;height:28px;font-size:12px}
.social{display:flex;gap:8px;margin-top:12px}
.social span{width:28px;height:28px;border-radius:50%;background:var(--navy-bar)}
.footer-bar{position:absolute;left:0;top:2430px;width:1200px;height:48px;background:var(--navy);color:var(--white);font-size:13px}
.footer-bar .copy{position:absolute;left:74px;top:16px}
.footer-bar nav a{position:absolute;top:16px}
</style>
</head>
<body>

<header class="site-header">
  <div class="brand">Kwelderhof Punt</div>
  <a class="btn btn-listed" href="#">Lawyers Get Listed</a>
</header>
<nav class="main-nav">
  <a class="is-active" style="left:74px">Home</a>
  <a style="left:156px">Find A Lawyer</a>
  <a style="left:282px">Question &amp; Answers</a>
  <a style="left:448px">Legal Practice Centers</a>
  <a style="left:622px">Code, Regulations &amp; Case Law</a>
  <a style="left:1010px">Sign in</a>
</nav>

<section class="hero" role="img" aria-label="Photo of a smiling couple consulting a lawyer at a desk">
  <div class="hero-panel">
    <h1 class="hero-title">Helping you with your<br>legal needs</h1>
    <div class="field field-search">Enter Legal Issue or Lawyer's Name</div>
    <div class="field field-province">Select Province
      <svg class="caret" width="18" height="12" viewBox="0 0 18 12"><path d="M0 0h18L9 12z" fill="#e8711a"/></svg>
    </div>
    <a class="btn btn-search" href="#">
      <svg width="26" height="26" viewBox="0 0 26 26"><circle cx="10" cy="10" r="7.5" fill="none" stroke="#fff" stroke-width="3"/><path d="M15.5 15.5l8 8" stroke="#fff" stroke-width="4" stroke-linecap="round"/></svg>
      SEARCH</a>
  </div>
</section>

<h2 class="finder-title" style="left:72px;top:768px">Find Lawyers by Location</h2>
<p class="finder-note">Either choose your location from the drop down or use the map</p>
<div class="select-small">Select Province
  <svg class="caret" style="top:15px;right:10px" width="12" height="8" viewBox="0 0 12 8"><path d="M0 0h12L6 8z" fill="#e8711a"/></svg>
</div>
<a class="btn btn-go" href="#">Go</a>
<div class="map-placeholder" role="img" aria-label="Clickable map of the Netherlands provinces with one province highlighted"></div>
<div class="divider"></div>

<h2 class="finder-title" style="left:572px;top:768px">Find Lawyers by Practice Area</h2>
<ul class="practice-list" style="top:814px">
  <li>Bankruptcy</li><li>Estate Planning</li><li>Personal Injury</li>
  <li>Business Law</li><li>Family Law</li><li>Probate</li>
  <li>Customer Law</li><li>Foreclosure Defense</li><li>Product Liability</li>
  <li>Criminal Law</li><li>Immigration Law</li><li>Real Estate law</li>
  <li>Divorce</li><li>Intelelctual Property</li><li>Tax Law</li>
  <li>DUI &amp; DWI</li><li>Medical Malpractice</li><li>Worker's Compensation</li>
  <li>Employment Law</li><li>Nursing home Abuse &amp; Neglect</li><li>Medical Malpractice</li>
  <li>Intelelctual Property</li><li>Probate</li><li>Product Liability</li>
  <li>Medical Malpractice</li><li>Product Liability</li><li class="more">more...</li>
</ul>

<h2 class="finder-title" style="left:572px;top:1090px">Find Lawyers by Practice Area</h2>
<ul class="practice-list" style="top:1138px">
  <li>Auto Accidents</li><li>Crminial Law</li><li>Personal Injury</li>
  <li>Business Law</li><li>Foreclosure</li><li>Probate</li>
  <li>Child Custody</li><li>Estate Planning</li><li>Product Liability</li>
  <li>Child Support</li><li>Family Law</li><li>Real Estate law</li>
  <li>Civil Rights</li><li>Divorce</li><li>Tax Law</li>
  <li>Consumer Law</li><li>Foreclosure Defense</li><li>Worker's Compensation</li>
  <li>Criminal Law</li><li>Immigration Law</li><li>Medical Malpractice</li>
  <li>Divorce</li><li>Intelelctual Property</li><li>Product Liability</li>
  <li>DUI &amp; DWI</li><li>Medical Malpractice</li><li class="more">more...</li>
</ul>

<section class="info-band" role="img" aria-label="Dark blue tinted photo of business people in a meeting">
  <h2>Free Legal Information on Kwelderhof Punt</h2>
  <div class="feature" style="left:56px">
    <svg width="70" height="64" viewBox="0 0 70 64"><rect x="0" y="0" width="46" height="34" rx="6" fill="#fff"/><path d="M8 34l-2 12 12-12z" fill="#fff"/><rect x="24" y="18" width="44" height="32" rx="6" fill="#fff" stroke="#173a72" stroke-width="3"/><path d="M58 50l4 12-14-12z" fill="#fff"/></svg>
    <h3>Questions &amp; Answers</h3>
    <p>Proin gravida nibh vel velit auctor aliquet enean sollicitudilorem quis bibendum auctor.</p>
  </div>
  <div class="feature" style="left:420px">
    <svg width="66" height="64" viewBox="0 0 66 64"><path d="M33 0L0 18h66z" fill="#fff"/><rect x="4" y="22" width="58" height="5" fill="#fff"/><g fill="#fff"><rect x="8" y="30" width="7" height="22"/><rect x="21" y="30" width="7" height="22"/><rect x="38" y="30" width="7" height="22"/><rect x="51" y="30" width="7" height="22"/></g><rect x="2" y="55" width="62" height="8" fill="#fff"/></svg>
    <h3>Legal Practice Centers</h3>
    <p>Proin gravida nibh vel velit auctor aliquet enean sollicitudilorem quis bibendum auctor.</p>
  </div>
  <div class="feature" style="left:780px">
    <svg width="64" height="64" viewBox="0 0 64 64"><rect x="22" y="10" width="20" height="10" rx="3" fill="none" stroke="#fff" stroke-width="4"/><rect x="2" y="18" width="60" height="40" rx="6" fill="#fff"/><rect x="14" y="18" width="4" height="40" fill="#173a72"/><rect x="46" y="18" width="4" height="40" fill="#173a72"/></svg>
    <h3>Codes, Regulations &amp; Case Law</h3>
    <p>Proin gravida nibh vel velit auctor aliquet enean sollicitudilorem quis bibendum auctor.</p>
  </div>
</section>

<h2 class="claim-title">Are you a Lawyer? Claim and Keep your Profile Updated</h2>
<p class="claim-text">Proin gravida nibh vel velit auctor aliquet enean sollicitudi lorem quis bibendum auctor nisi elit consequat ipsum nec sagittis sem nibh id elit uis sed odio sit amet nibh vulputate cursus a sit amet mauris.</p>
<a class="btn btn-claim" href="#">Get Listed Now</a>
<div class="rule"></div>

<footer>
  <div class="footer-col" style="left:74px">
    <h4>About Us</h4>
    <ul><li>Company History</li><li>Privacy</li><li>Careers</li><li>Community Guidelines</li><li>Media</li></ul>
  </div>
  <div class="footer-col" style="left:326px">
    <h4>Legal Information</h4>
    <ul><li>Questions &amp; Answers</li><li>Legal Practice Center</li><li>Code &amp; Regulation</li><li>Case Law</li><li>How to choose a lawyer</li></ul>
  </div>
  <div class="footer-col" style="left:642px">
    <h4>Lawyers</h4>
    <ul><li>Get Listed</li><li>Update Profile</li><li>Get Support</li><li>Contact Us</li><li>Terms &amp; Conditions</li></ul>
  </div>
  <div class="footer-col" style="left:896px">
    <h4 style="margin-bottom:2px">Newsletter</h4>
    <p class="footer-note">Get the latest News &amp; Listing</p>
    <div class="news-form"><div class="news-input">Your Email Address</div><div class="btn news-send">Send</div></div>
    <h4 style="margin:16px 0 0">Connect with us</h4>
    <div class="social" aria-label="Social network links"><span></span><span></span><span></span><span></span></div>
  </div>
  <div class="footer-bar">
    <span class="copy">Kwelderhof Punt © 2015 All Rights Reserved</span>
    <nav>
      <a style="left:516px">Find A Lawyer</a>
      <a style="left:628px">Question &amp; Answers</a>
      <a style="left:778px">Legal Practice Centers</a>
      <a style="left:940px">Code, Regulations &amp; Case Law</a>
    </nav>
  </div>
</footer>

</body>
</html>
```